new KVR one page flyer

We need a 1 page A4 size flyer (need it asap please) that describes on 1 page with art work and using photos the services we provide. I have included some examples of old previous flyers from our other (seperate divisions of the business) I have named a photo called (photo for top of design) however you do your design this photo needs to be the star of the page by either having it at the top or bottom of the page please and we usually like this photo to be in greyscale colour.
we do like greyscale designs but are open to see what you come up with as a whole page of grey white and black might not suit.

Needs to list the following

Services include:
Over size loads / Hot Shot Loads
Heavy Vehicle Recovery services
Potable Water Deliveries
Road Building / Maintenance
Earthworks
Sand & Metal Supply & Cartage
Road Train Tippers
Road Train Tankers
Road Train Flat Tops
Drop Deck Trailers
Mine site accredited equipment & Operators.

We offer a large rage of services not listed so call us today for a personalised quote to suit your needs.

To go on the bottom of the page our contact details are

KVR Pty Ltd
Depot: Lot 514, Banksia Flats Track Coober Pedy
Mobile: 047 216 9381
email: darren@kestrelvaleroadworks.com.au

Target Market(s)

new clients

Colors

Designer to choose colors to be used in the design.

Requirements
Must have
• our services listed
Nice to have
• stand out designs

```html
<!DOCTYPE html>
<html lang="en">
<head>
<meta charset="utf-8">
<title>KVR Pty Ltd – Services Flyer</title>
<link href="https://fonts.googleapis.com/css2?family=Jost:wght@400;500&display=swap" rel="stylesheet">
<style>
  :root {
    --backdrop: #14303d;
    --paper: #ffffff;
    --ink: #23232b;
    --ink-soft: #3a3a44;
    --band-dark: #1c1a26;
    --band-mid: #3b3548;
    --sky-top: #8f8dc8;
    --sky-low: #c9cbe2;
    --sand: #c9b8a3;
    --grey-block: #5c5c64;
    --text-light: #f2f2f5;
    --rule: rgba(255,255,255,0.35);
  }
  * { margin: 0; padding: 0; box-sizing: border-box; }
  html, body { width: 1200px; height: 1200px; overflow: hidden; }
  body {
    background: var(--backdrop);
    font-family: "Jost", "Futura", sans-serif;
    color: var(--ink);
  }
  .flyer {
    position: absolute;
    left: 197px; top: 30px;
    width: 806px; height: 1140px;
    background: var(--paper);
    overflow: hidden;
  }
  .hero-photo {
    position: absolute; inset: 0 0 auto 0; height: 640px;
    background: linear-gradient(180deg, var(--sky-top) 0%, var(--sky-low) 40%, var(--sand) 70%, #ffffff 100%);
  }
  .hero-fade {
    position: absolute; left: 0; right: 0; top: 380px; height: 260px;
    background: linear-gradient(180deg, rgba(255,255,255,0) 0%, rgba(255,255,255,0.85) 55%, #fff 100%);
  }
  .corner-shape { position: absolute; left: 0; top: 0; }
  .brand {
    position: absolute; left: 48px; top: 150px;
    font-size: 96px; font-weight: 500; letter-spacing: 4px;
    color: var(--ink-soft); line-height: 1;
  }
  .title {
    position: absolute; left: 0; right: 0; top: 440px;
    text-align: center; text-transform: uppercase;
    font-weight: 500; color: var(--ink); line-height: 1.02;
    white-space: nowrap;
  }
  .title .line-1 { display: block; font-size: 70px; color: var(--ink-soft); }
  .title .line-2 { display: block; font-size: 74px; }
  .services-heading {
    position: absolute; left: 0; right: 0; top: 612px;
    text-align: center; font-size: 46px; font-weight: 400; color: var(--ink-soft);
  }
  .services-band {
    position: absolute; left: 0; right: 0; top: 690px; height: 270px;
    background: linear-gradient(180deg, var(--band-mid) 0%, var(--band-dark) 100%);
    display: flex; padding: 30px 30px 0;
  }
  .services-col {
    flex: 1; list-style: none; padding: 0 22px;
    color: var(--text-light); font-size: 19px; line-height: 34px;
    white-space: nowrap;
  }
  .services-col + .services-col { border-left: 1px solid var(--rule); }
  .services-col li { display: flex; align-items: flex-start; gap: 10px; }
  .services-col li svg { flex: none; margin-top: 11px; }
  .quote-strip {
    position: absolute; left: 0; right: 0; top: 960px; height: 70px;
    background: var(--paper);
    display: flex; align-items: center; justify-content: center; text-align: center;
    font-size: 17px; font-weight: 500; text-transform: uppercase; letter-spacing: 0.5px;
    color: var(--ink); line-height: 1.35; padding: 0 40px;
  }
  .contact-bar {
    position: absolute; left: 0; right: 0; bottom: 0; height: 110px;
    background: var(--band-dark);
    display: flex; align-items: center; color: var(--text-light);
  }
  .contact-phone {
    flex: none; height: 100%; width: 380px;
    background: linear-gradient(90deg, var(--grey-block), #47454f);
    display: flex; align-items: center; gap: 16px; padding-left: 32px;
    font-size: 38px; font-weight: 500; letter-spacing: 1px; white-space: nowrap;
  }
  .contact-item {
    flex: 1; min-width: 0; display: flex; flex-direction: column; align-items: center; gap: 6px;
    font-size: 13px; text-align: center; line-height: 1.3; padding: 0 8px;
    white-space: nowrap;
  }
  .contact-item + .contact-item { border-left: 1px solid var(--rule); }
  .contact-item strong { font-weight: 500; }
</style>
</head>
<body>
<main class="flyer">
  <div class="hero-photo" role="img" aria-label="Photo of a white road train tanker truck parked on an outback dirt yard under a blue sky, shown in soft tones"></div>
  <div class="hero-fade"></div>
  <svg class="corner-shape" width="806" height="640" aria-hidden="true">
    <polygon points="0,0 380,0 0,380" fill="rgba(255,255,255,0.28)"/>
  </svg>
  <div class="brand">KVR</div>

  <h1 class="title">
    <span class="line-1">Kestrel Vale</span>
    <span class="line-2">Roadworks</span>
  </h1>
  <h2 class="services-heading">Services include:</h2>

  <section class="services-band" role="img" aria-label="Dark-toned photo of heavy trucks at a depot behind the services list">
    <ul class="services-col">
      <li><svg width="12" height="12"><circle cx="6" cy="6" r="5" fill="none" stroke="#f2f2f5" stroke-width="1.5"/></svg>Over size loads / Hot Shot Loads</li>
      <li><svg width="12" height="12"><circle cx="6" cy="6" r="5" fill="none" stroke="#f2f2f5" stroke-width="1.5"/></svg>Heavy Vehicle Recovery services</li>
      <li><svg width="12" height="12"><circle cx="6" cy="6" r="5" fill="none" stroke="#f2f2f5" stroke-width="1.5"/></svg>Potable Water Deliveries</li>
      <li><svg width="12" height="12"><circle cx="6" cy="6" r="5" fill="none" stroke="#f2f2f5" stroke-width="1.5"/></svg>Road Building / Maintenance</li>
      <li><svg width="12" height="12"><circle cx="6" cy="6" r="5" fill="none" stroke="#f2f2f5" stroke-width="1.5"/></svg>Earthworks</li>
      <li><svg width="12" height="12"><circle cx="6" cy="6" r="5" fill="none" stroke="#f2f2f5" stroke-width="1.5"/></svg>Drop Deck Trailers</li>
    </ul>
    <ul class="services-col">
      <li><svg width="12" height="12"><circle cx="6" cy="6" r="5" fill="none" stroke="#f2f2f5" stroke-width="1.5"/></svg>Sand &amp; Metal Supply &amp; Cartage</li>
      <li><svg width="12" height="12"><circle cx="6" cy="6" r="5" fill="none" stroke="#f2f2f5" stroke-width="1.5"/></svg>Road Train Tippers</li>
      <li><svg width="12" height="12"><circle cx="6" cy="6" r="5" fill="none" stroke="#f2f2f5" stroke-width="1.5"/></svg>Road Train Tankers</li>
      <li><svg width="12" height="12"><circle cx="6" cy="6" r="5" fill="none" stroke="#f2f2f5" stroke-width="1.5"/></svg>Road Train Flat Tops</li>
      <li><svg width="12" height="12"><circle cx="6" cy="6" r="5" fill="none" stroke="#f2f2f5" stroke-width="1.5"/></svg><span>Mine site accredited<br>equipment &amp; Operators.</span></li>
    </ul>
  </section>

  <p class="quote-strip">We offer a large rage of services not listed so call us today for<br>a personalised quote to suit your needs.</p>

  <footer class="contact-bar">
    <div class="contact-phone">
      <svg width="44" height="44" viewBox="0 0 44 44" aria-hidden="true">
        <circle cx="22" cy="22" r="19" fill="none" stroke="#f2f2f5" stroke-width="2.5"/>
        <path d="M15 13c2-1 3 0 4 2l1 3c0 1-1 2-2 3 1 3 3 5 6 6 1-1 2-2 3-2l3 1c2 1 3 2 2 4-1 2-3 3-5 2-7-2-12-7-14-14-1-2 0-4 2-5z" fill="#f2f2f5"/>
      </svg>
      <span>047 216 9381</span>
    </div>
    <div class="contact-item">
      <svg width="20" height="26" viewBox="0 0 20 26" aria-hidden="true">
        <path d="M10 0C4.5 0 0 4.3 0 9.6 0 16.8 10 26 10 26s10-9.2 10-16.4C20 4.3 15.5 0 10 0z" fill="#f2f2f5"/>
        <circle cx="10" cy="9.5" r="3.6" fill="#1c1a26"/>
      </svg>
      <span>Lot 514, Banksia Flats Track<br>Coober Pedy</span>
    </div>
    <div class="contact-item">
      <svg width="28" height="20" viewBox="0 0 28 20" aria-hidden="true">
        <rect x="1" y="1" width="26" height="18" fill="none" stroke="#f2f2f5" stroke-width="2"/>
        <path d="M1 1l13 10L27 1" fill="none" stroke="#f2f2f5" stroke-width="2"/>
      </svg>
      <span>darren@<strong>kestrelvaleroadworks</strong>.com.au</span>
    </div>
  </footer>
</main>
</body>
</html>
```